Business card for my new company (Accounting firm)

I need a business card for my new business Corvane Advisory and Ledger SA. Our services are accounting, tax, audit and financial management. Our customers are small companies, start-ups and new companies. The final design has to show financial security, trust and growth. Please find our logo attached to the business card. Text for the business card: Corvane Advisory and Ledger SA Tomas da Varela Director and Founder Certified Accountant Tel. 022 418 27 35 tv@corvaneconseil.ch www.corvaneconseil.ch Rue des Vergers-Bleus 14 1201 Geneva
Target Market(s)
Our customers are small companies, start-ups and new companies.
Industry/Entity Type
Finance And Accounting
Contact Information for Business Card
Corvane Conseil et Registre SA
Tomas da Varela
Directeur et Fondateur
Expert-comptable diplômé
Tél. 022 418 27 35
tv@corvaneconseil.ch
www.corvaneconseil.ch
Rue des Vergers-Bleus 14
1201 Genève

```html
<!DOCTYPE html>
<html lang="fr">
<head>
<meta charset="utf-8">
<title>Corvane Conseil et Registre SA – carte de visite</title>
<link rel="stylesheet" href="https://fonts.googleapis.com/css2?family=Didact+Gothic&display=swap">
<style>
  :root {
    --backdrop: #cfe0ef;
    --card-white: #ffffff;
    --brand-blue: #0555a5;
    --ink-blue: #0b4fa3;
    --soft-blue: #3d7cc4;
  }
  * { margin: 0; padding: 0; box-sizing: border-box; }
  html, body {
    width: 1200px;
    height: 840px;
    overflow: hidden;
    background: var(--backdrop);
    font-family: "Didact Gothic", "Helvetica Neue", Arial, sans-serif;
  }
  .canvas {
    position: relative;
    width: 1200px;
    height: 840px;
  }
  .card {
    position: absolute;
    top: 252px;
    width: 560px;
    height: 335px;
    overflow: hidden;
    box-shadow: 0 6px 18px rgba(40, 70, 110, 0.12);
  }
  .card--front { left: 30px; background: var(--card-white); color: var(--ink-blue); }
  .card--back { left: 610px; background: var(--brand-blue); }

  .brand-mark {
    position: absolute;
    display: flex;
    align-items: center;
    gap: 7px;
    font-size: 17px;
    letter-spacing: 0.12em;
  }
  .brand-mark__square { width: 12px; height: 12px; }
  .card--front .brand-mark { left: 54px; top: 66px; color: var(--ink-blue); }
  .card--front .brand-mark__square { background: var(--ink-blue); }
  .card--back .brand-mark { right: 38px; top: 80px; color: var(--card-white); }
  .card--back .brand-mark__square { background: var(--card-white); }

  .holder { position: absolute; left: 54px; top: 166px; }
  .holder__name { font-size: 20px; letter-spacing: 0.02em; }
  .holder__title {
    margin-top: 9px;
    font-size: 12px;
    font-style: italic;
    line-height: 1.4;
    color: var(--soft-blue);
  }

  .company { position: absolute; left: 297px; top: 66px; }
  .company__name { font-size: 29px; line-height: 1.08; letter-spacing: 0.02em; }
  .contact {
    margin-top: 30px;
    list-style: none;
    font-size: 19px;
    line-height: 24.5px;
    letter-spacing: 0.01em;
  }

  .back-graphic {
    position: absolute;
    left: 0;
    top: 0;
    width: 240px;
    height: 335px;
    background: linear-gradient(100deg, #ffffff 0%, #e4eef8 40%, #6f9fd3 78%, var(--brand-blue) 100%);
  }
</style>
</head>
<body>
<main class="canvas">
  <section class="card card--front" aria-label="Recto de la carte">
    <div class="brand-mark"><span class="brand-mark__square"></span><span>CORVANE</span></div>

    <div class="holder">
      <p class="holder__name">Tomas da Varela</p>
      <p class="holder__title">Directeur et Fondateur/<br>Expert-comptable diplômé</p>
    </div>

    <div class="company">
      <h1 class="company__name">Corvane Conseil<br>et Registre SA</h1>
      <ul class="contact">
        <li>022 418 27 35</li>
        <li>tv@corvaneconseil.ch</li>
        <li>www.corvaneconseil.ch</li>
        <li>Rue des Vergers-Bleus 14</li>
        <li>1201 Genève</li>
      </ul>
    </div>
  </section>

  <section class="card card--back" aria-label="Verso de la carte">
    <div class="back-graphic" role="img" aria-label="Grand motif graphique de la marque en blanc sur bleu"></div>
    <div class="brand-mark"><span class="brand-mark__square"></span><span>CORVANE</span></div>
  </section>
</main>
</body>
</html>
```